Health & Beauty Company- Business Card Design

Two-sided business card design and logo design.

Company markets and sells otc treatments for the health and beauty industry. Marketing products to doctors, pharmacists and retail drug companies like tormundos, pqz and lumo fex.

Designs should be submitted as vector based PDFs. To keep your text in vector format, our printer recommends applications like Adobe Illustrator, Adobe InDesign and more recent versions of Adobe Photoshop.

Target Market(s)

Drug stores, doctors and pharmacists

Industry/Entity Type

Printer

Requirements
Must have
• Back side of business card should include company logo and our tagline: "Advancing Everyday Wellness & Care Solutions"

Company name acronym must be included: QTRM

```html
<!DOCTYPE html>
<html lang="en">
<head>
<meta charset="utf-8">
<title>QTRM Business Card</title>
<link href="https://fonts.googleapis.com/css2?family=Open+Sans:wght@400;600;700&display=swap" rel="stylesheet">
<style>
  :root {
    --page-bg: #e3e3eb;
    --card-top: #ffffff;
    --card-bottom: #e9e9e9;
    --ink: #1e1e1e;
    --ink-soft: #555555;
    --mark-tone: #d6d6d6;
    --rule: #444444;
  }
  html, body {
    margin: 0;
    padding: 0;
    width: 1200px;
    height: 900px;
    overflow: hidden;
    background: var(--page-bg);
    font-family: "Open Sans", Arial, sans-serif;
    color: var(--ink);
  }
  .canvas {
    position: relative;
    width: 1200px;
    height: 900px;
  }
  .card {
    position: absolute;
    width: 500px;
    height: 286px;
    background: linear-gradient(160deg, var(--card-top) 0%, var(--card-bottom) 100%);
    box-shadow: 0 6px 18px rgba(0,0,0,0.12);
    overflow: hidden;
  }
  .card--front { left: 70px; top: 307px; }
  .card--back { left: 630px; top: 307px; }

  /* Front side */
  .brand {
    position: absolute;
    left: 70px;
    top: 108px;
    display: flex;
    align-items: center;
    gap: 18px;
  }
  .brand__dot {
    width: 58px;
    height: 58px;
    border-radius: 50%;
    background: var(--ink);
  }
  .brand__text { display: flex; flex-direction: column; }
  .brand__name {
    font-weight: 700;
    font-size: 40px;
    line-height: 1;
    letter-spacing: 1px;
  }
  .brand__tagline {
    font-weight: 600;
    font-size: 11.5px;
    margin-top: 4px;
    white-space: nowrap;
  }

  /* Back side */
  .back-mark {
    position: absolute;
    left: 150px;
    top: 30px;
    width: 220px;
    height: 220px;
    border-radius: 50%;
    background: radial-gradient(circle, var(--mark-tone) 0%, rgba(214,214,214,0.35) 60%, rgba(214,214,214,0) 75%);
  }
  .identity {
    position: absolute;
    left: 30px;
    top: 98px;
    text-align: right;
    width: 215px;
  }
  .identity__name {
    font-weight: 700;
    font-size: 18px;
    margin: 0;
  }
  .identity__role {
    font-size: 9px;
    color: var(--ink-soft);
    margin: 2px 0 6px;
  }
  .identity__address {
    font-size: 9px;
    color: var(--ink-soft);
    margin: 0;
    white-space: nowrap;
  }
  .divider {
    position: absolute;
    left: 262px;
    top: 90px;
    width: 1px;
    height: 110px;
    background: var(--rule);
  }
  .contacts {
    position: absolute;
    left: 282px;
    top: 104px;
    list-style: none;
    margin: 0;
    padding: 0;
    font-size: 13px;
    color: var(--ink);
  }
  .contacts li {
    display: flex;
    align-items: center;
    gap: 9px;
    height: 20px;
    white-space: nowrap;
  }
  .contacts svg { width: 12px; height: 12px; fill: var(--ink); flex: none; }
</style>
</head>
<body>
<main class="canvas">
  <section class="card card--front" aria-label="Card front">
    <div class="brand">
      <span class="brand__dot"></span>
      <div class="brand__text">
        <span class="brand__name">QTRM</span>
        <span class="brand__tagline">Advancing Everyday Wellness &amp; Care Solutions</span>
      </div>
    </div>
  </section>

  <section class="card card--back" aria-label="Card back">
    <div class="back-mark" role="img" aria-label="Faint company emblem in the background"></div>
    <div class="identity">
      <p class="identity__name">Marisa Keller</p>
      <p class="identity__role">President &amp; CEO</p>
      <p class="identity__address">123 Versatile Street Ave, City, State, Zipcode</p>
    </div>
    <div class="divider"></div>
    <ul class="contacts">
      <li>
        <svg viewBox="0 0 12 12"><path d="M3 1h2l1 3-1.5 1a6 6 0 0 0 2.5 2.5L8 6l3 1v2a1 1 0 0 1-1 1A9 9 0 0 1 2 2a1 1 0 0 1 1-1z"/></svg>
        +000.000.0000
      </li>
      <li>
        <svg viewBox="0 0 12 12"><rect x="3" y="1" width="6" height="3"/><rect x="1" y="4" width="10" height="5" rx="1"/><rect x="3" y="8" width="6" height="3"/></svg>
        +000.000.0000
      </li>
      <li>
        <svg viewBox="0 0 12 12"><path d="M1 2.5h10v7H1z"/><path d="M1 2.5l5 4 5-4" fill="none" stroke="#fff" stroke-width="1"/></svg>
        youname@email.com
      </li>
      <li>
        <svg viewBox="0 0 12 12"><circle cx="6" cy="6" r="5"/></svg>
        chat.username
      </li>
    </ul>
  </section>
</main>
</body>
</html>
```